Business Card Design

The name of my business is called Brisk Lantern, Inc.

We are the first brick and mortar store in our state that will specialize in spy equipment. I don't want the term "spy equipment" used in the design of the card. I would like a double sided card with the one side having all my contact information and the other side having the company name and the quote "Discreet Surveillance Equipment". I'm not looking for the perfect card on the first try but am not looking to make many changes.

I would like the card to speak sophistication so I tend to lean toward dark color backgrounds.

Industry/Entity Type

Store

Contact Information for Business Card

Harold Dumbrell, Consultant
555-318-0927
harold.dumbrell@brisklantern.example
www.brisklantern.example

```html
<!DOCTYPE html>
<html lang="en">
<head>
<meta charset="utf-8">
<title>Brisk Lantern, Inc. — Business Card</title>
<link rel="stylesheet" href="https://fonts.googleapis.com/css2?family=Bebas+Neue&family=Montserrat:wght@300;400&display=swap">
<style>
  :root {
    --backdrop: #dcdcdc;
    --ink-dark: #070b14;
    --sand: #bdb28a;
    --berry: #9b1f4f;
    --slate: #2b3340;
    --white: #ffffff;
  }
  html, body {
    margin: 0;
    padding: 0;
    width: 1200px;
    height: 900px;
    overflow: hidden;
    background: var(--backdrop);
  }
  .sheet {
    position: relative;
    width: 1200px;
    height: 900px;
    display: flex;
    flex-direction: column;
    align-items: center;
    justify-content: center;
    gap: 50px;
  }
  .card {
    position: relative;
    width: 630px;
    height: 360px;
    background: var(--sand);
    overflow: hidden;
    box-shadow: 0 6px 18px rgba(0,0,0,0.18);
  }
  .card-shape {
    position: absolute;
    inset: 0;
    width: 100%;
    height: 100%;
  }
  .card-shape .dark-field { fill: var(--ink-dark); }
  .card-shape .edge-line { fill: none; stroke: var(--berry); stroke-width: 2; }

  .brand {
    position: absolute;
    right: 32px;
    top: 130px;
  }
  .brand-name {
    font-family: "Bebas Neue", sans-serif;
    font-size: 54px;
    line-height: 0.9;
    letter-spacing: 1px;
    color: var(--slate);
    margin: 0;
  }
  .brand-tagline {
    font-family: "Montserrat", sans-serif;
    font-weight: 400;
    font-size: 15px;
    color: var(--slate);
    margin: 3px 0 0 10px;
    white-space: nowrap;
  }
  .card--back .brand { top: 140px; right: 28px; }

  .person {
    position: absolute;
    left: 32px;
    top: 40px;
  }
  .person-rule {
    display: flex;
    width: 140px;
    height: 4px;
    margin-bottom: 6px;
  }
  .person-rule .rule-berry { flex: 1.15; background: var(--berry); }
  .person-rule .rule-sand { flex: 1; background: var(--sand); }
  .person-name {
    font-family: "Bebas Neue", sans-serif;
    font-size: 30px;
    line-height: 1;
    color: var(--white);
    margin: 0;
    letter-spacing: 0.5px;
    white-space: nowrap;
  }
  .person-role {
    font-family: "Bebas Neue", sans-serif;
    font-size: 18px;
    line-height: 1;
    color: var(--sand);
    margin: 2px 0 0 12px;
    letter-spacing: 0.5px;
  }

  .contact {
    position: absolute;
    left: 0;
    bottom: 34px;
    display: flex;
    align-items: stretch;
  }
  .contact-bar {
    width: 22px;
    background: var(--berry);
  }
  .contact-list {
    list-style: none;
    margin: 0;
    padding: 4px 0 4px 14px;
    font-family: "Bebas Neue", sans-serif;
    font-size: 18px;
    line-height: 1.45;
    color: var(--sand);
    letter-spacing: 0.5px;
    white-space: nowrap;
  }
</style>
</head>
<body>
  <main class="sheet">

    <section class="card card--front" aria-label="Card front">
      <svg class="card-shape" viewBox="0 0 630 360" preserveAspectRatio="none" aria-hidden="true">
        <path class="dark-field" d="M0,0 H205 C232,0 238,50 248,95 C262,150 290,175 320,210 C355,250 375,305 410,360 H0 Z"/>
        <path class="edge-line" d="M205,0 C232,0 238,50 248,95 C262,150 290,175 320,210 C355,250 375,305 410,360"/>
      </svg>
      <div class="brand">
        <p class="brand-name">Brisk Lantern</p>
        <p class="brand-tagline">Discreet Surveillance Equipment</p>
      </div>
    </section>

    <section class="card card--back" aria-label="Card back">
      <svg class="card-shape" viewBox="0 0 630 360" preserveAspectRatio="none" aria-hidden="true">
        <path class="dark-field" d="M0,0 H205 C232,0 238,50 248,95 C262,150 290,175 320,210 C355,250 375,305 410,360 H0 Z"/>
        <path class="edge-line" d="M205,0 C232,0 238,50 248,95 C262,150 290,175 320,210 C355,250 375,305 410,360"/>
      </svg>
      <div class="person">
        <div class="person-rule"><span class="rule-berry"></span><span class="rule-sand"></span></div>
        <p class="person-name">Harold Dumbrell</p>
        <p class="person-role">Consultant</p>
      </div>
      <div class="contact">
        <span class="contact-bar"></span>
        <ul class="contact-list">
          <li>555-318-0927</li>
          <li>harold.dumbrell@brisklantern.example</li>
          <li>www.brisklantern.example</li>
        </ul>
      </div>
      <div class="brand">
        <p class="brand-name">Brisk Lantern</p>
        <p class="brand-tagline">Discreet Surveillance Equipment</p>
      </div>
    </section>

  </main>
</body>
</html>
```